Business Card Design for new logo

Business card Design for new logo. Follow colors from logo.
The company has offices in multiple comtries
Want to have some bulltes on the countries and also on the main services

Something like
USA*Dominican Republic*LATAM

Consulting*Healthcare IT*Tranformation

Industry/Entity Type

Information Technology

Contact Information for Business Card

Address, Phones, countries, name and position

Lucan morrel

Founder and CEO

947 Tarrow Ln
Brennick, PA 17460

Lmorrel@quendoxcare.com

www.quendoxcare.com

555-304-6182

555-222-2222

```html
<!DOCTYPE html>
<html lang="en">
<head>
<meta charset="utf-8">
<title>Quendox Care – Business Cards</title>
<link href="https://fonts.googleapis.com/css2?family=Open+Sans:wght@400;600&family=Marcellus&display=swap" rel="stylesheet">
<style>
  :root{
    --bg:#d9d9d9;
    --card:#ffffff;
    --blue:#2a74b5;
    --orange:#f28c4f;
    --ink:#3a3a3a;
    --map:#ececec;
  }
  *{margin:0;padding:0;box-sizing:border-box}
  html,body{width:1200px;height:900px;overflow:hidden}
  body{background:var(--bg);font-family:"Open Sans",Arial,sans-serif;position:relative}

  .card{position:absolute;width:540px;height:310px;background:var(--card);border-radius:26px;overflow:hidden;box-shadow:0 6px 18px rgba(0,0,0,.18)}

  /* front card */
  .card--front{left:70px;top:90px}
  .front__map{position:absolute;left:30px;top:20px;width:480px;height:200px;border-radius:40px;
    background:radial-gradient(ellipse at center,var(--map) 0%,rgba(236,236,236,.4) 60%,rgba(255,255,255,0) 100%)}
  .front__brand{position:absolute;left:0;right:0;top:88px;display:flex;justify-content:center;align-items:center;gap:14px}
  .brand-dot{width:30px;height:30px;border-radius:50%;background:var(--orange)}
  .brand-name{font-family:"Marcellus",Georgia,serif;font-size:50px;color:var(--blue);line-height:1}
  .front__services{position:absolute;left:0;right:0;top:168px;text-align:center;font-size:16px;letter-spacing:.5px;color:var(--ink)}
  .dot{display:inline-block;width:9px;height:9px;border-radius:50%;margin:0 8px;vertical-align:middle}
  .dot--orange{background:var(--orange)}
  .dot--white{background:#fff}
  .front__band{position:absolute;left:0;right:0;bottom:0;height:72px;background:var(--blue);
    display:flex;align-items:center;justify-content:center;color:#fff;font-size:16px;letter-spacing:.5px}

  /* back card */
  .card--back{left:590px;top:480px}
  .back__shape{position:absolute;inset:0}
  .back__brand{position:absolute;left:34px;top:38px;font-family:"Marcellus",Georgia,serif;font-size:36px;font-weight:400;line-height:1.2;color:var(--blue)}
  .back__person{position:absolute;left:34px;top:92px}
  .person-name{font-size:21px;font-weight:600;color:var(--blue);line-height:1.2}
  .person-role{font-size:15px;color:var(--orange);line-height:1.3}
  .back__details{position:absolute;left:34px;top:192px;color:#fff;font-size:14px;line-height:1.25}
  .address{margin-bottom:6px}
  .contact{list-style:none}
  .contact li{display:flex;align-items:center;gap:9px}
  .contact svg{width:12px;height:12px;flex:none}
</style>
</head>
<body>

<section class="card card--front">
  <div class="front__map" role="img" aria-label="Faint dotted world map"></div>
  <div class="front__brand">
    <span class="brand-dot"></span>
    <span class="brand-name">Quendox Care</span>
  </div>
  <p class="front__services">Consulting<span class="dot dot--orange"></span>Healthcare IT<span class="dot dot--orange"></span>Tranformation</p>
  <div class="front__band">USA<span class="dot dot--white"></span>Dominican Republic<span class="dot dot--white"></span>LATAM</div>
</section>

<section class="card card--back">
  <svg class="back__shape" viewBox="0 0 540 310" preserveAspectRatio="none" aria-hidden="true">
    <polygon points="0,182 540,100 540,310 0,310" fill="var(--orange)"/>
  </svg>
  <h1 class="back__brand">Quendox Care</h1>
  <div class="back__person">
    <p class="person-name">Lucan morrel</p>
    <p class="person-role">Founder and CEO</p>
  </div>
  <div class="back__details">
    <p class="address">947 Tarrow Ln<br>Brennick, PA 17460</p>
    <ul class="contact">
      <li><svg viewBox="0 0 16 16"><path d="M3 2h3l1.5 4-2 1.2a9 9 0 0 0 3.3 3.3L10 8.5l4 1.5v3c0 .6-.4 1-1 1A12 12 0 0 1 2 3c0-.6.4-1 1-1z" fill="#fff"/></svg>555-304-6182</li>
      <li><svg viewBox="0 0 16 16"><rect x="4" y="1" width="8" height="14" rx="1.5" fill="none" stroke="#fff" stroke-width="1.6"/></svg>555-222-2222</li>
      <li><svg viewBox="0 0 16 16"><rect x="1" y="3" width="14" height="10" fill="#fff"/><path d="M1 3l7 6 7-6" fill="none" stroke="var(--orange)" stroke-width="1.4"/></svg>Lmorrel@quendoxcare.com</li>
      <li><svg viewBox="0 0 16 16"><circle cx="8" cy="8" r="7" fill="#fff"/><path d="M4.5 8.5l2.3 2.3 4.7-5" fill="none" stroke="var(--orange)" stroke-width="1.6"/></svg>www.quendoxcare.com</li>
    </ul>
  </div>
</section>

</body>
</html>
```